Velvet Afterhours Poster Design

Need poster design made up in next few days, can guarantee payment to winner. Poster must contain the following but feel free to word it better:
Velvet Afterhours
Presented by quenmor Sound
Select resident djs
Drink specials all night
Open from 8pm to 12pm
Find us on Chatterbox
At Larkfield Suites every Saturday
These will be on posters and fliers
Of a3 and roughly a5 size.
Our target audience is people 18-25
We want the posters to be exciting and professional. We would like a blue or purple with black color scheme but there is plenty of room for creative license so have a play around with what you think looks good. We currently don't have a logo but if your including one we would like to see it as m4 as in marble as an element. Our first drink special is cocktails in jars but is not essential to include, can provide proper copy of the picture if you want to include it in your design. Please contact us if you need more information. we will be quick to pick a winner so payment will be provided fast!!!
Thank you all in advance for your submissions!!

```html
<!DOCTYPE html>
<html lang="en">
<head>
<meta charset="utf-8">
<title>Velvet Afterhours – Saturday Club Night</title>
<link rel="stylesheet" href="https://fonts.googleapis.com/css2?family=Anton&family=Righteous&display=swap">
<style>
  :root {
    --night: #000000;
    --steel: #9fb6c4;
    --steel-light: #c9dbe5;
    --steel-dark: #3a2f44;
    --violet-glow: #c05ad0;
    --badge: #8f2b8f;
    --badge-ring: #1a1a1a;
    --grid-line: #1d1d1d;
    --mesh: #d8d8d8;
    --white: #ffffff;
    --lavender: #b9b6f5;
    --gold-edge: #f2e23a;
  }
  * { margin: 0; padding: 0; box-sizing: border-box; }
  html, body { width: 1200px; height: 849px; overflow: hidden; background: var(--night); }

  .poster {
    position: relative;
    width: 1200px;
    height: 849px;
    overflow: hidden;
    background: var(--night);
    font-family: "Righteous", sans-serif;
  }

  .element-grid {
    position: absolute;
    left: 680px; top: 0;
    width: 540px; height: 720px;
  }

  .wire-mesh {
    position: absolute;
    right: 0; top: 0;
    width: 600px; height: 849px;
    background:
      radial-gradient(ellipse 260px 420px at 100% 45%, rgba(216,216,216,0.16), transparent 70%),
      radial-gradient(ellipse 340px 120px at 40% 95%, rgba(216,216,216,0.14), transparent 70%);
  }

  .glow {
    position: absolute;
    left: 230px; top: 250px;
    width: 420px; height: 220px;
    background: radial-gradient(ellipse at center, rgba(192,90,208,0.95) 0%, rgba(150,50,170,0.5) 35%, transparent 70%);
    filter: blur(6px);
  }

  .title {
    position: absolute;
    left: 60px; top: 40px;
    width: 760px;
    perspective: 900px;
  }
  .title__word {
    display: block;
    font-family: "Anton", sans-serif;
    font-weight: 400;
    color: var(--steel);
    line-height: 0.95;
    letter-spacing: -2px;
    transform-origin: left center;
    text-shadow:
      2px 2px 0 var(--steel-dark), 4px 4px 0 var(--steel-dark),
      6px 6px 0 var(--steel-dark), 8px 8px 0 var(--steel-dark),
      10px 10px 0 #2a2233, 12px 12px 0 #231c2b,
      14px 14px 18px rgba(0,0,0,0.8);
    background: linear-gradient(180deg, var(--steel-light), var(--steel));
    -webkit-background-clip: text;
  }
  .title__word--first {
    font-size: 250px;
    transform: rotateY(24deg) rotateZ(-3deg) scaleX(1.05);
    margin-left: 40px;
  }
  .title__word--second {
    font-size: 220px;
    transform: rotateY(24deg) rotateZ(-3deg) scaleX(0.92);
    margin-top: 0;
  }

  .presenter {
    position: absolute;
    left: 470px; top: 712px;
    font-family: "Anton", sans-serif;
    font-size: 22px;
    color: var(--white);
    letter-spacing: 0.5px;
    transform: rotate(-9deg);
    text-shadow: 2px 2px 0 #000;
  }

  .badge {
    position: absolute;
    left: 860px; top: 250px;
    width: 300px; height: 300px;
  }
  .badge__text {
    position: absolute;
    left: 35px; top: 55px;
    width: 230px;
    text-align: center;
    color: var(--white);
    font-size: 17px;
    line-height: 1.9;
    text-transform: uppercase;
  }
  .badge__text .hours { font-size: 24px; line-height: 1.35; margin-top: 4px; display: block; }

  .venue-line {
    position: absolute;
    right: 14px; top: 772px;
    font-size: 41px;
    letter-spacing: 0.5px;
    text-transform: uppercase;
    color: var(--lavender);
    -webkit-text-stroke: 1.6px var(--gold-edge);
    text-shadow: 0 0 6px rgba(60,60,200,0.6);
    white-space: nowrap;
  }
</style>
</head>
<body>
<main class="poster">
  <svg class="element-grid" viewBox="0 0 540 720" aria-hidden="true">
    <g stroke="var(--grid-line)" stroke-width="1.5" fill="none">
      <path d="M220 20 H540 M220 100 H540 M0 180 H540 M0 260 H540 M0 340 H540 M0 420 H540 M0 500 H540 M80 560 H540 M80 640 H540 M80 720 H540"/>
      <path d="M0 180 V500 M80 180 V720 M160 180 V720 M240 20 V720 M320 20 V720 M400 20 V720 M480 20 V720"/>
    </g>
  </svg>

  <div class="wire-mesh" role="img" aria-label="Fine white wireframe curves sweeping from the right edge down to the bottom corner"></div>

  <div class="glow"></div>

  <h1 class="title">
    <span class="title__word title__word--first">Velvet</span>
    <span class="title__word title__word--second">Afterhours</span>
  </h1>

  <p class="presenter">Presented by quenmor Sound</p>

  <div class="badge">
    <svg width="300" height="300" viewBox="0 0 300 300" aria-hidden="true">
      <circle cx="150" cy="150" r="124" fill="var(--badge)" stroke="var(--badge-ring)" stroke-width="6"/>
      <defs>
        <path id="badge-arc" d="M22 170 A130 130 0 0 0 278 150" />
      </defs>
    </svg>
    <p class="badge__text">
      Select resident DJ's<br>
      Drink specials all night
      <span class="hours">Open from<br>8pm to 12pm</span>
    </p>
    <svg width="300" height="300" viewBox="0 0 300 300" style="position:absolute;left:0;top:0" aria-hidden="false">
      <path id="find-arc" d="M10 175 A142 142 0 0 0 290 130" fill="none"/>
      <text font-family="Righteous, sans-serif" font-size="19" fill="var(--white)" letter-spacing="1">
        <textPath href="#find-arc" startOffset="22%">FIND US ON CHATTERBOX</textPath>
      </text>
    </svg>
  </div>

  <p class="venue-line">At Larkfield Suites every Saturday</p>
</main>
</body>
</html>
```